Revamp Current Website From 2012 TO 2018

We need a ravamp to our current website. I prefer a professional corporate modern feel to it.

My Current Website is www.brightlanepromoworks.biz. Please redesign the homepage and the /certs page first....see attached document for specific instructions..

There is a lot of content at the bottom but maybe we can shorten that by using titles and a pop up of the details or something so it doesnt take too mcuh space...or maybe a red more hyperlink to see the rest of info in pop up or something or new page...

Target Market(s)

B2B, business owners, website owners, marketing companies.

Industry/Entity Type

Promotional Product

Number of Pages Required

2 page

Colors

Designer to choose colors to be used in the design.

Requirements
Must have
• Please keep in mind logo mock up I am working on that looks beautiful on dark background for header...see attached for logo
• Must use existing content I hope your marketing mind comes in to play when designing the website.
• Must have all my content provided on each page...
Nice to have
• similiar color scheme...
Should not have
• I dont like using templates because usually hard to expand on design in future so Prefer full custom designs
• Please no templates

```html
<!DOCTYPE html>
<html lang="en">
<head>
<meta charset="utf-8">
<title>Our Incentives – Brightlane Promo Works</title>
<link href="https://fonts.googleapis.com/css2?family=Source+Sans+3:wght@400;600;700&display=swap" rel="stylesheet">
<style>
:root{
  --page-bg:#292525;
  --topbar-bg:#1e1b1b;
  --panel-bg:#ececec;
  --card-body:#dcdcdc;
  --card-image:#1d2024;
  --brand-blue:#1e78c8;
  --title-blue:#1f73bf;
  --pill-dark:#151515;
  --text-dark:#3a3a3a;
  --text-light:#ffffff;
  --muted:#7d7a7a;
}
*{box-sizing:border-box;margin:0;padding:0}
html,body{width:1200px;height:4337px;overflow:hidden}
body{background:var(--page-bg);font-family:"Source Sans 3",Arial,sans-serif;position:relative;color:var(--text-dark)}

.topbar{position:absolute;top:0;left:0;width:1200px;height:30px;background:var(--topbar-bg);display:flex;align-items:center;padding:0 90px;font-size:11px;color:#cfcfcf}
.topbar .contact{display:flex;gap:6px;align-items:center}
.topbar .account{margin-left:auto;display:flex;gap:8px;align-items:center}
.field{width:150px;height:18px;border-radius:9px;background:#f2f2f2;color:#8a8a8a;font-size:10px;padding:0 10px;display:flex;align-items:center;justify-content:center}
.btn-small{height:18px;border-radius:9px;background:var(--brand-blue);color:#fff;font-size:10px;padding:0 14px;display:flex;align-items:center}
.btn-small.dark{background:#0f0f0f;border:1px solid #555}

.site-header{position:absolute;top:30px;left:0;width:1200px;height:62px;display:flex;align-items:center;padding:0 90px}
.brand{display:flex;align-items:center;gap:10px;color:var(--brand-blue);font-weight:700;font-size:17px;letter-spacing:.5px}
.brand .mark{width:22px;height:22px;background:var(--brand-blue)}
.main-nav{margin-left:auto;display:flex;gap:30px;font-size:12px;color:#e6e6e6;text-transform:uppercase}
.main-nav .active{color:var(--brand-blue);border-bottom:2px solid var(--brand-blue);padding-bottom:3px}

.hero{position:absolute;top:116px;left:61px;width:1078px;height:208px;background:linear-gradient(100deg,#2f2d33 0%,#4a4052 40%,#6b5478 65%,#cfc9d3 90%,#f1f0f2 100%);display:flex;align-items:center;padding-left:29px}
.hero h1{color:var(--text-light);font-size:44px;font-weight:700;letter-spacing:.5px}

.category-nav{position:absolute;top:356px;left:61px;width:1078px;height:173px;background:var(--brand-blue);display:grid;grid-template-columns:repeat(3,318px);column-gap:32px;row-gap:20px;padding:49px 29px 0}
.category-nav a{height:48px;border-radius:24px;background:var(--pill-dark);color:var(--brand-blue);font-size:16px;font-weight:700;text-decoration:none;display:flex;align-items:center;justify-content:center}
.category-nav a:nth-child(4){color:#8fc6f5}

.incentive-group{position:absolute;left:61px;width:1078px;background:var(--panel-bg);padding:48px 29px 0}
.incentive-group h2{color:var(--title-blue);font-size:42px;font-weight:700;line-height:46px;margin-bottom:57px}
.card-grid{display:grid;grid-template-columns:repeat(4,234px);column-gap:29px;row-gap:35px}
.card{height:312px;background:var(--card-body)}
.card-image{height:185px;background:linear-gradient(180deg,#2a3035 0%,var(--card-image) 100%);position:relative}
.card-image span{position:absolute;left:0;right:0;bottom:10px;text-align:center;color:var(--brand-blue);font-size:11px;font-weight:700}
.card-body{padding:8px 10px 0;height:127px;position:relative;font-size:11px;line-height:13px;color:var(--text-dark)}
.card-body p{height:52px;overflow:hidden}
.more{position:absolute;right:10px;bottom:9px;height:22px;border-radius:11px;background:var(--brand-blue);color:#fff;font-size:10px;font-weight:600;padding:0 6px 0 10px;display:flex;align-items:center;gap:5px}
.more svg{width:11px;height:11px}

.site-footer{position:absolute;top:4193px;left:61px;width:1078px;display:flex;font-size:13px;color:var(--muted)}
.site-footer nav{margin-left:auto;color:var(--brand-blue)}
.site-footer nav a{color:var(--brand-blue);text-decoration:none}
</style>
</head>
<body>

<div class="topbar">
  <div class="contact">
    <svg width="9" height="11" viewBox="0 0 9 11"><path d="M2 0h2l1 3-1.5 1c.6 1.4 1.4 2.3 2.5 3L7 5.5 9 7v2c-4.5 0-9-4-9-9z" fill="#1e78c8"/></svg>
    <span>(555) 013-2218 (USA Office)</span>
    <span>|</span>
    <span>(555) 019-4410 (International)</span>
  </div>
  <div class="account">
    <div class="field">Username</div>
    <div class="field">Password</div>
    <div class="btn-small dark">Login</div>
    <div class="btn-small">Sign Up</div>
  </div>
</div>

<header class="site-header">
  <div class="brand"><span class="mark"></span>Brightlane Promo Works</div>
  <nav class="main-nav">
    <span>Home</span><span class="active">Our Incentives</span><span>Samples</span><span>How It Works</span><span>Testimonials</span><span>FAQ</span><span>Contact</span>
  </nav>
</header>

<section class="hero" role="img" aria-label="Banner photograph of an abstract purple geometric architectural ceiling">
  <h1>OUR INCENTIVES</h1>
</section>

<nav class="category-nav">
  <a>Vacation Certificates</a>
  <a>Electronic Product Certificates</a>
  <a>Dining Certificates</a>
  <a>Gas &amp; Grocery Cash Back Rewards</a>
  <a>Medical &amp; RX Discount Certificates</a>
  <a>Coming Soon</a>
</nav>

<section class="incentive-group" style="top:607px;height:1225px">
  <h2>Vacation Certificates</h2>
  <div class="card-grid">
    <article class="card"><div class="card-image" role="img" aria-label="Photo of an airplane and hotel"><span>Airfare &amp; Hotel - U.S. ONLY</span></div><div class="card-body"><p>Lorem ipsum dolor sit amet, consetetur sadipscing elitr, sed diam nonumy eirmod tempor invidunt ut labore et dolore magna aliquyam erat, sed diam voluptua. At vero eos et accusam et justo duo dolores et ea</p><div class="more">More Details <svg viewBox="0 0 11 11"><circle cx="5.5" cy="5.5" r="5.5" fill="#fff"/><path d="M4.5 3l2.5 2.5L4.5 8" stroke="#1e78c8" stroke-width="1.4" fill="none"/></svg></div></div></article>
    <article class="card"><div class="card-image" role="img" aria-label="Photo of a resort condo"><span>7 Night Resort Condo - 3500 + Locations</span></div><div class="card-body"><p>rebum. Stet clita kasd gubergren, no sea takimata sanctus est Lorem ipsum dolor sit amet. Lorem ipsum dolor sit amet, consetetur sadipscing elitr, sed diam nonumy eirmod tempor invidunt ut labore et dolore</p><div class="more">More Details <svg viewBox="0 0 11 11"><circle cx="5.5" cy="5.5" r="5.5" fill="#fff"/><path d="M4.5 3l2.5 2.5L4.5 8" stroke="#1e78c8" stroke-width="1.4" fill="none"/></svg></div></div></article>
    <article class="card"><div class="card-image" role="img" aria-label="Photo of a Las Vegas hotel at night"><span>3-4 Night Las Vegas Hotel &amp; Casino</span></div><div class="card-body"><p>magna aliquyam erat, sed diam voluptua. At vero eos et accusam et justo duo dolores et ea rebum. Stet clita kasd gubergren, no sea takimata sanctus est Lorem ipsum dolor sit amet. Lorem ipsum dolor sit amet, consetetur</p><div class="more">More Details <svg viewBox="0 0 11 11"><circle cx="5.5" cy="5.5" r="5.5" fill="#fff"/><path d="M4.5 3l2.5 2.5L4.5 8" stroke="#1e78c8" stroke-width="1.4" fill="none"/></svg></div></div></article>
    <article class="card"><div class="card-image" role="img" aria-label="Photo of a Mexican beach resort"><span>Luxurious Mexico Beach Resort</span></div><div class="card-body"><p>tur sadipscing elitr, sed diam nonumy eirmod tempor invidunt ut labore et dolore magna aliquyam erat, sed diam voluptua. At vero eos et accusam et justo duo dolores et ea rebum. Stet clita kasd gubergren, no sea</p><div class="more">More Details <svg viewBox="0 0 11 11"><circle cx="5.5" cy="5.5" r="5.5" fill="#fff"/><path d="M4.5 3l2.5 2.5L4.5 8" stroke="#1e78c8" stroke-width="1.4" fill="none"/></svg></div></div></article>
    <article class="card"><div class="card-image" role="img" aria-label="Photo of a golf course by the sea"><span>Golf N' Stay In Cabo San Lucas</span></div><div class="card-body"><p>Lorem ipsum dolor sit amet, consetetur sadipscing elitr, sed diam nonumy eirmod tempor invidunt ut labore et dolore magna aliquyam erat, sed diam voluptua. At vero eos et accusam et justo duo dolores et ea</p><div class="more">More Details <svg viewBox="0 0 11 11"><circle cx="5.5" cy="5.5" r="5.5" fill="#fff"/><path d="M4.5 3l2.5 2.5L4.5 8" stroke="#1e78c8" stroke-width="1.4" fill="none"/></svg></div></div></article>
    <article class="card"><div class="card-image" role="img" aria-label="Photo of a hotel room"><span>1 Night Hotel Stay</span></div><div class="card-body"><p>rebum. Stet clita kasd gubergren, no sea takimata sanctus est Lorem ipsum dolor sit amet. Lorem ipsum dolor sit amet, consetetur sadipscing elitr, sed diam nonumy eirmod tempor invidunt ut labore et dolore</p><div class="more">More Details <svg viewBox="0 0 11 11"><circle cx="5.5" cy="5.5" r="5.5" fill="#fff"/><path d="M4.5 3l2.5 2.5L4.5 8" stroke="#1e78c8" stroke-width="1.4" fill="none"/></svg></div></div></article>
    <article class="card"><div class="card-image" role="img" aria-label="Photo of a hotel room"><span>2 Night Hotel Stay</span></div><div class="card-body"><p>magna aliquyam erat, sed diam voluptua. At vero eos et accusam et justo duo dolores et ea rebum. Stet clita kasd gubergren, no sea takimata sanctus est Lorem ipsum dolor sit amet. Lorem ipsum dolor sit amet, consetetur</p><div class="more">More Details <svg viewBox="0 0 11 11"><circle cx="5.5" cy="5.5" r="5.5" fill="#fff"/><path d="M4.5 3l2.5 2.5L4.5 8" stroke="#1e78c8" stroke-width="1.4" fill="none"/></svg></div></div></article>
    <article class="card"><div class="card-image" role="img" aria-label="Photo of a hotel room"><span>3 Night Hotel Stay</span></div><div class="card-body"><p>tur sadipscing elitr, sed diam nonumy eirmod tempor invidunt ut labore et dolore magna aliquyam erat, sed diam voluptua. At vero eos et accusam et justo duo dolores et ea rebum. Stet clita kasd gubergren, no sea</p><div class="more">More Details <svg viewBox="0 0 11 11"><circle cx="5.5" cy="5.5" r="5.5" fill="#fff"/><path d="M4.5 3l2.5 2.5L4.5 8" stroke="#1e78c8" stroke-width="1.4" fill="none"/></svg></div></div></article>
    <article class="card"><div class="card-image" role="img" aria-label="Photo of a hotel room"><span>4 Night Hotel Stay</span></div><div class="card-body"><p>Lorem ipsum dolor sit amet, consetetur sadipscing elitr, sed diam nonumy eirmod tempor invidunt ut labore et dolore magna aliquyam erat, sed diam voluptua. At vero eos et accusam et justo duo dolores et ea</p><div class="more">More Details <svg viewBox="0 0 11 11"><circle cx="5.5" cy="5.5" r="5.5" fill="#fff"/><path d="M4.5 3l2.5 2.5L4.5 8" stroke="#1e78c8" stroke-width="1.4" fill="none"/></svg></div></div></article>
  </div>
</section>

<section class="incentive-group" style="top:1867px;height:546px">
  <h2>Electronic Product Certificates</h2>
  <div class="card-grid">
    <article class="card"><div class="card-image" role="img" aria-label="Photo of a tablet computer"><span>7-inch Wi-Fi Tablets</span></div><div class="card-body"><p>Lorem ipsum dolor sit amet, consetetur sadipscing elitr, sed diam nonumy eirmod tempor invidunt ut labore et dolore magna aliquyam erat, sed diam voluptua. At vero eos et accusam et justo duo dolores et ea</p><div class="more">More Details <svg viewBox="0 0 11 11"><circle cx="5.5" cy="5.5" r="5.5" fill="#fff"/><path d="M4.5 3l2.5 2.5L4.5 8" stroke="#1e78c8" stroke-width="1.4" fill="none"/></svg></div></div></article>
    <article class="card"><div class="card-image" role="img" aria-label="Photo of a touch media player"><span>Touch Mp4 Player</span></div><div class="card-body"><p>rebum. Stet clita kasd gubergren, no sea takimata sanctus est Lorem ipsum dolor sit amet. Lorem ipsum dolor sit amet, consetetur sadipscing elitr, sed diam nonumy eirmod tempor invidunt ut labore et dolore</p><div class="more">More Details <svg viewBox="0 0 11 11"><circle cx="5.5" cy="5.5" r="5.5" fill="#fff"/><path d="M4.5 3l2.5 2.5L4.5 8" stroke="#1e78c8" stroke-width="1.4" fill="none"/></svg></div></div></article>
    <article class="card"><div class="card-image" role="img" aria-label="Photo of a digital camcorder"><span>Mini Digital Camcorder</span></div><div class="card-body"><p>magna aliquyam erat, sed diam voluptua. At vero eos et accusam et justo duo dolores et ea rebum. Stet clita kasd gubergren, no sea takimata sanctus est Lorem ipsum dolor sit amet. Lorem ipsum dolor sit amet, consetetur</p><div class="more">More Details <svg viewBox="0 0 11 11"><circle cx="5.5" cy="5.5" r="5.5" fill="#fff"/><path d="M4.5 3l2.5 2.5L4.5 8" stroke="#1e78c8" stroke-width="1.4" fill="none"/></svg></div></div></article>
    <article class="card"><div class="card-image" role="img" aria-label="Photo of earbuds"><span>New Premium Quality Earbuds</span></div><div class="card-body"><p>tur sadipscing elitr, sed diam nonumy eirmod tempor invidunt ut labore et dolore magna aliquyam erat, sed diam voluptua. At vero eos et accusam et justo duo dolores et ea rebum. Stet clita kasd gubergren, no sea</p><div class="more">More Details <svg viewBox="0 0 11 11"><circle cx="5.5" cy="5.5" r="5.5" fill="#fff"/><path d="M4.5 3l2.5 2.5L4.5 8" stroke="#1e78c8" stroke-width="1.4" fill="none"/></svg></div></div></article>
  </div>
</section>

<section class="incentive-group" style="top:2448px;height:543px">
  <h2>Dining Certificates</h2>
  <div class="card-grid">
    <article class="card"><div class="card-image" role="img" aria-label="Photo of a restaurant table"><span>Premium $25 Restaurant Gift Certificate</span></div><div class="card-body"><p>Lorem ipsum dolor sit amet, consetetur sadipscing elitr, sed diam nonumy eirmod tempor invidunt ut labore et dolore magna aliquyam erat, sed diam voluptua. At vero eos et accusam et justo duo dolores et ea</p><div class="more">More Details <svg viewBox="0 0 11 11"><circle cx="5.5" cy="5.5" r="5.5" fill="#fff"/><path d="M4.5 3l2.5 2.5L4.5 8" stroke="#1e78c8" stroke-width="1.4" fill="none"/></svg></div></div></article>
    <article class="card"><div class="card-image" role="img" aria-label="Photo of a plated restaurant meal"><span>$100 Restaurant Certificate</span></div><div class="card-body"><p>rebum. Stet clita kasd gubergren, no sea takimata sanctus est Lorem ipsum dolor sit amet. Lorem ipsum dolor sit amet, consetetur sadipscing elitr, sed diam nonumy eirmod tempor invidunt ut labore et dolore</p><div class="more">More Details <svg viewBox="0 0 11 11"><circle cx="5.5" cy="5.5" r="5.5" fill="#fff"/><path d="M4.5 3l2.5 2.5L4.5 8" stroke="#1e78c8" stroke-width="1.4" fill="none"/></svg></div></div></article>
  </div>
</section>

<section class="incentive-group" style="top:3026px;height:563px">
  <h2>Gas &amp; Grocery Cash Back Rewards<br>Available As Premium Only</h2>
  <div class="card-grid" style="margin-top:-20px">
    <article class="card"><div class="card-image" role="img" aria-label="Photo of grocery shopping"><span>Premium $25 Cash Back Reward - Groceries</span></div><div class="card-body"><p>Lorem ipsum dolor sit amet, consetetur sadipscing elitr, sed diam nonumy eirmod tempor invidunt ut labore et dolore magna aliquyam erat, sed diam voluptua. At vero eos et accusam et justo duo dolores et ea</p><div class="more">More Details <svg viewBox="0 0 11 11"><circle cx="5.5" cy="5.5" r="5.5" fill="#fff"/><path d="M4.5 3l2.5 2.5L4.5 8" stroke="#1e78c8" stroke-width="1.4" fill="none"/></svg></div></div></article>
    <article class="card"><div class="card-image" role="img" aria-label="Photo of a gas pump"><span>Premium $50 Cash Back Reward - Gas</span></div><div class="card-body"><p>rebum. Stet clita kasd gubergren, no sea takimata sanctus est Lorem ipsum dolor sit amet. Lorem ipsum dolor sit amet, consetetur sadipscing elitr, sed diam nonumy eirmod tempor invidunt ut labore et dolore</p><div class="more">More Details <svg viewBox="0 0 11 11"><circle cx="5.5" cy="5.5" r="5.5" fill="#fff"/><path d="M4.5 3l2.5 2.5L4.5 8" stroke="#1e78c8" stroke-width="1.4" fill="none"/></svg></div></div></article>
    <article class="card"><div class="card-image" role="img" aria-label="Photo of grocery shopping"><span>Premium $100 Cash Back Reward - Groc</span></div><div class="card-body"><p>magna aliquyam erat, sed diam voluptua. At vero eos et accusam et justo duo dolores et ea rebum. Stet clita kasd gubergren, no sea takimata sanctus est Lorem ipsum dolor sit amet. Lorem ipsum dolor sit amet, consetetur</p><div class="more">More Details <svg viewBox="0 0 11 11"><circle cx="5.5" cy="5.5" r="5.5" fill="#fff"/><path d="M4.5 3l2.5 2.5L4.5 8" stroke="#1e78c8" stroke-width="1.4" fill="none"/></svg></div></div></article>
    <article class="card"><div class="card-image" role="img" aria-label="Photo of a gas pump"><span>Premium $50 Cash Back Reward - Gas</span></div><div class="card-body"><p>tur sadipscing elitr, sed diam nonumy eirmod tempor invidunt ut labore et dolore magna aliquyam erat, sed diam voluptua. At vero eos et accusam et justo duo dolores et ea rebum. Stet clita kasd gubergren, no sea</p><div class="more">More Details <svg viewBox="0 0 11 11"><circle cx="5.5" cy="5.5" r="5.5" fill="#fff"/><path d="M4.5 3l2.5 2.5L4.5 8" stroke="#1e78c8" stroke-width="1.4" fill="none"/></svg></div></div></article>
  </div>
</section>

<section class="incentive-group" style="top:3624px;height:552px">
  <h2>Medical &amp; RX Discount Certificates</h2>
  <div class="card-grid">
    <article class="card"><div class="card-image" role="img" aria-label="Photo of a healthcare discount card"><span>Free Healthcare Discount Card</span></div><div class="card-body"><p>Lorem ipsum dolor sit amet, consetetur sadipscing elitr, sed diam nonumy eirmod tempor invidunt ut labore et dolore magna aliquyam erat, sed diam voluptua. At vero eos et accusam et justo duo dolores et ea</p><div class="more">More Details <svg viewBox="0 0 11 11"><circle cx="5.5" cy="5.5" r="5.5" fill="#fff"/><path d="M4.5 3l2.5 2.5L4.5 8" stroke="#1e78c8" stroke-width="1.4" fill="none"/></svg></div></div></article>
  </div>
</section>

<footer class="site-footer">
  <span>© 2005-2014 Brightlane Promo Works, Inc. - All Rights Reserved</span>
  <nav><a>Affiliate Program</a> | <a>Terms &amp; Conditions</a> | <a>Privacy Policy</a> | <a>Login</a></nav>
</footer>

</body>
</html>
```